New Business Card Design Project

We would like a business card that represents the sale of boat, home, auto, and life insurance.

The logo can change colors to meet the look of the design if needed.

Industry/Entity Type

Business

```html
<!DOCTYPE html>
<html lang="en">
<head>
<meta charset="utf-8">
<title>Harbourline Financial – Business Card</title>
<link href="https://fonts.googleapis.com/css2?family=Questrial&family=Libre+Baskerville:wght@400;700&display=swap" rel="stylesheet">
<style>
  :root{
    --bg:#2c2c2c;
    --card:#f7f7f7;
    --blue:#3b7489;
    --ink:#4a4a4a;
    --dark:#262626;
    --light:#ffffff;
  }
  html,body{margin:0;padding:0;overflow:hidden;}
  body{width:1200px;height:997px;background:var(--bg);position:relative;}
  .card{position:absolute;width:560px;height:320px;background:var(--card);overflow:hidden;
        box-shadow:0 10px 30px rgba(0,0,0,.5);}
  .card--back{left:25px;top:338px;}
  .card--front{left:615px;top:338px;}
  .card__bands{position:absolute;left:0;top:0;width:560px;height:320px;}
  .brand{position:absolute;left:0;width:560px;display:flex;justify-content:center;align-items:center;gap:12px;
         font-family:"Questrial",sans-serif;color:var(--ink);letter-spacing:.18em;font-size:26px;}
  .brand__dot{width:18px;height:18px;border-radius:50%;background:var(--blue);}
  .card--back .brand{top:110px;}
  .card--front .brand{top:60px;}
  .website{position:absolute;left:0;width:560px;top:205px;text-align:center;
           font-family:"Libre Baskerville",serif;font-weight:700;font-size:13px;letter-spacing:.08em;color:var(--ink);}
  .person{position:absolute;left:50px;top:190px;font-family:"Libre Baskerville",serif;}
  .person__name{color:var(--blue);font-weight:700;font-size:19px;margin:0;}
  .person__role{color:var(--ink);font-size:15px;margin:4px 0 0;}
  .divider{position:absolute;left:282px;top:160px;width:3px;height:70px;background:var(--dark);}
  .contact{position:absolute;left:322px;top:150px;font-family:"Libre Baskerville",serif;font-size:12px;color:var(--ink);}
  .contact__row{display:flex;align-items:center;gap:10px;height:24px;}
  .contact__row svg{width:14px;height:14px;fill:var(--blue);}
  .address{position:absolute;right:28px;top:248px;text-align:left;font-family:"Libre Baskerville",serif;
           font-size:13px;color:var(--light);line-height:1.45;letter-spacing:.03em;}
</style>
</head>
<body>

<section class="card card--back">
  <svg class="card__bands" viewBox="0 0 560 320" aria-hidden="true">
    <path d="M0 248 H150 C175 248 180 290 205 290 H560 V320 H0 Z" fill="var(--blue)"/>
  </svg>
  <div class="brand"><span class="brand__dot"></span>HARBOURLINE FINANCIAL</div>
  <div class="website">www.harbourlinecover.com.au</div>
</section>

<section class="card card--front">
  <svg class="card__bands" viewBox="0 0 560 320" aria-hidden="true">
    <path d="M0 284 H300 C325 284 325 228 350 228 H560 V236 H352 C330 236 330 296 305 296 H0 Z" fill="var(--dark)"/>
    <path d="M0 296 H305 C330 296 330 236 352 236 H560 V320 H0 Z" fill="var(--blue)"/>
  </svg>
  <div class="brand"><span class="brand__dot"></span>HARBOURLINE FINANCIAL</div>

  <div class="person">
    <p class="person__name">DAN HOLLIS</p>
    <p class="person__role">MANAGING DIRECTOR</p>
  </div>

  <div class="divider"></div>

  <div class="contact">
    <div class="contact__row">
      <svg viewBox="0 0 24 24" aria-hidden="true"><path d="M6.6 10.8a15 15 0 0 0 6.6 6.6l2.2-2.2a1 1 0 0 1 1-.25 11.4 11.4 0 0 0 3.6.57 1 1 0 0 1 1 1V20a1 1 0 0 1-1 1A17 17 0 0 1 3 4a1 1 0 0 1 1-1h3.5a1 1 0 0 1 1 1c0 1.25.2 2.45.57 3.6a1 1 0 0 1-.25 1z"/></svg>
      <span>+61 412 555 019</span>
    </div>
    <div class="contact__row">
      <svg viewBox="0 0 24 24" aria-hidden="true"><path d="M2 5h20v14H2z M2 5l10 8 10-8" fill="var(--blue)" stroke="var(--card)" stroke-width="1.5"/></svg>
      <span>dan@harbourline.com.au</span>
    </div>
  </div>

  <div class="address">48 QUAY STREET<br>BALLINA, NSW 2478</div>
</section>

</body>
</html>
```